Branvique needs a business Card Design

We are looking for a business card Design for our new Managed Service Provider Company, Branvique. Branvique encompasses everything IT for the average medium sized business. Our primary services are help desk support, cyber-security (malware and ransomware protection), and Disaster Recovery systems. We would like the design to have a very clean and professional look, with a very minimalist feel.

Target Market(s)

Medium to large sized businesses

Industry/Entity Type

It Service

Contact Information for Business Card

Name GoesHere
name@branvique.com
O: 555-382-6047
C: 555-731-5820

Font styles to use
Other font styles liked:
• Poppins Font Only Please

Colors

Designer to choose only greyscale colors for use in the design.

Requirements
Must have
• Logo included
Nice to have
• Cutting Edge, innovative, minimalistic, elegant

```html
<!DOCTYPE html>
<html lang="en">
<head>
<meta charset="utf-8">
<title>Branvique Business Card</title>
<link href="https://fonts.googleapis.com/css2?family=Poppins:wght@300;400;500;600&display=swap" rel="stylesheet">
<style>
  :root {
    --page: #fefefe;
    --card-light: #f4f4f4;
    --navy: #12233f;
    --ink: #0f1c30;
    --white: #ffffff;
  }
  html, body {
    margin: 0;
    padding: 0;
    width: 1200px;
    height: 1200px;
    overflow: hidden;
    background: var(--page);
    font-family: "Poppins", sans-serif;
  }
  .canvas {
    position: relative;
    width: 1200px;
    height: 1200px;
  }
  .card-front {
    position: absolute;
    left: 339px;
    top: 252px;
    width: 523px;
    height: 339px;
    background: var(--card-light);
    overflow: hidden;
  }
  .front-info {
    position: absolute;
    left: 0;
    right: 0;
    top: 0;
    text-align: center;
    color: var(--ink);
  }
  .brand-mark {
    display: inline-flex;
    align-items: center;
    gap: 10px;
  }
  .brand-dot {
    width: 18px;
    height: 18px;
    border-radius: 50%;
  }
  .front-info .brand-dot { background: var(--ink); margin-top: 50px; }
  .front-info .brand-name {
    display: block;
    margin-top: 48px;
    font-weight: 500;
    font-size: 27px;
    letter-spacing: 13px;
    padding-left: 13px;
    line-height: 1;
  }
  .person {
    margin-top: 22px;
    font-size: 20px;
    font-weight: 300;
    line-height: 1;
  }
  .person strong { font-weight: 500; }
  .email {
    margin-top: 15px;
    font-size: 20px;
    font-weight: 500;
    line-height: 1;
  }
  .phones {
    margin-top: 15px;
    font-size: 20px;
    font-weight: 300;
    line-height: 1;
  }
  .phones b { font-weight: 600; }
  .phones .gap { display: inline-block; width: 10px; }
  .front-band {
    position: absolute;
    left: 0;
    bottom: 0;
    width: 523px;
    height: 44px;
  }
  .card-back {
    position: absolute;
    left: 339px;
    top: 610px;
    width: 523px;
    height: 338px;
    background: var(--navy);
    color: var(--white);
    text-align: center;
  }
  .card-back .brand-dot { background: var(--white); }
  .back-logo {
    position: absolute;
    left: 0;
    right: 0;
    top: 110px;
  }
  .back-logo .brand-name {
    display: block;
    margin-top: 42px;
    font-weight: 500;
    font-size: 29px;
    letter-spacing: 14px;
    padding-left: 14px;
    line-height: 1;
  }
  .website {
    margin-top: 8px;
    font-size: 15px;
    font-weight: 300;
    letter-spacing: 3px;
    line-height: 1;
  }
</style>
</head>
<body>
<main class="canvas">
  <section class="card-front">
    <div class="front-info">
      <div class="brand-mark"><span class="brand-dot"></span></div>
      <span class="brand-name">BRANVIQUE</span>
      <div class="person">Name <strong>Last Name</strong></div>
      <div class="email">name@branvique.com</div>
      <div class="phones"><b>O:</b> 555-382-6047<span class="gap"></span><b>C:</b> 555-731-5820</div>
    </div>
    <svg class="front-band" viewBox="0 0 523 44" role="img" aria-label="Navy band with subtle decorative pattern">
      <path d="M0 44 L20 18 Q40 0 70 0 L523 0 L523 44 Z" fill="#12233f"/>
    </svg>
  </section>

  <section class="card-back" role="img" aria-label="Navy card back with subtle decorative pattern">
    <div class="back-logo">
      <div class="brand-mark"><span class="brand-dot"></span></div>
      <span class="brand-name">BRANVIQUE</span>
      <div class="website">www.branvique.com</div>
    </div>
  </section>
</main>
</body>
</html>
```